Business Card Design Project 4 Construction Business

I am after a creative, but sleek and simple/ clean business card design. This design will form the basis of future items and might include a logo or simply a creative way to lay out the text of my company name 'kestrel ventures'
I like the simplicity of black and white however I would also be happy to see a splash of colour introduced somehow to give the text some interest and make it stand out.
I would like a double sided card.
I am young (ish!) and professional, offering construction and project management services, what I don't want is the traditional builders type card featuring a cheesy hammer/ saw image etc.
As the company name, kestrel ventures, suggests, we focus on working closely and collaboratively together, in synergy with all stakeholders involved in the projects that we undertake
Construction

```html
<!DOCTYPE html>
<html lang="en">
<head>
<meta charset="utf-8">
<title>Kestrel Ventures Business Card</title>
<link href="https://fonts.googleapis.com/css2?family=Exo+2:wght@400;700&family=Titillium+Web:wght@400&display=swap" rel="stylesheet">
<style>
  :root {
    --stage: #d9d9d9;
    --card-dark: #2b2d30;
    --card-dark-edge: #1c1d1f;
    --card-light: #ffffff;
    --band-dark: #2f3134;
    --accent: #1e7fc1;
    --accent-deep: #1469a6;
    --ink-light: #ffffff;
    --ink-muted: #cfe4f3;
    --ink-grey: #6d6f72;
  }
  * { box-sizing: border-box; margin: 0; padding: 0; }
  html, body { width: 1200px; height: 861px; overflow: hidden; }
  body {
    background: var(--stage);
    display: flex;
    align-items: center;
    justify-content: center;
    gap: 60px;
    font-family: "Exo 2", sans-serif;
  }
  .card {
    position: relative;
    width: 520px;
    height: 300px;
    border-radius: 16px;
    overflow: hidden;
    box-shadow: 0 6px 18px rgba(0,0,0,0.18);
  }
  /* Front */
  .card--front {
    background: linear-gradient(135deg, #3a3c40 0%, var(--card-dark) 45%, var(--card-dark-edge) 100%);
  }
  .front-tab {
    position: absolute;
    left: 57%;
    right: 0;
    top: 40%;
    height: 28%;
    background: linear-gradient(180deg, #2a8fd2, var(--accent-deep));
    border-radius: 8px 0 0 8px;
    display: flex;
    flex-direction: column;
    justify-content: center;
    padding-left: 22px;
  }
  .wordmark {
    color: var(--ink-light);
    font-weight: 700;
    text-transform: uppercase;
    line-height: 1.05;
  }
  .front-tab .wordmark { font-size: 27px; letter-spacing: 0.5px; }
  .front-tab .wordmark span { display: block; font-size: 15px; letter-spacing: 5px; }
  /* Back */
  .card--back {
    background: linear-gradient(160deg, var(--card-light) 55%, #e6e6e6 100%);
  }
  .back-band {
    position: absolute;
    left: 0; right: 0;
    top: 17%;
    height: 14%;
    background: var(--band-dark);
  }
  .name-block {
    position: absolute;
    left: 0;
    top: 17%;
    width: 56%;
    height: 19%;
    background: linear-gradient(180deg, #2a8fd2, var(--accent-deep));
    border-radius: 0 6px 6px 0;
    padding: 7px 0 0 54px;
    color: var(--ink-light);
  }
  .name-block .person { font-size: 27px; font-weight: 700; text-transform: uppercase; line-height: 1.05; }
  .name-block .role { font-size: 13px; color: var(--ink-muted); text-transform: uppercase; }
  .contact-list {
    position: absolute;
    left: 0;
    top: 52%;
    list-style: none;
    font-family: "Titillium Web", sans-serif;
    font-size: 11.5px;
    color: var(--ink-light);
  }
  .contact-list li {
    background: var(--band-dark);
    border-right: 4px solid var(--accent);
    height: 18px;
    line-height: 18px;
    padding-left: 48px;
    margin-bottom: 6px;
  }
  .contact-list .address { width: 280px; }
  .contact-list .phone { width: 135px; }
  .contact-list .email { width: 218px; }
  .contact-list .web { width: 210px; }
  .back-mark {
    position: absolute;
    right: 22px;
    top: 62%;
    color: var(--accent);
    font-weight: 700;
    text-transform: uppercase;
    font-size: 26px;
    line-height: 1.05;
    text-align: left;
  }
  .back-mark span { display: block; font-size: 15px; letter-spacing: 5px; }
</style>
</head>
<body>
  <section class="card card--front" aria-label="Card front">
    <div class="front-tab">
      <div class="wordmark">Kestrel<span>Ventures</span></div>
    </div>
  </section>

  <section class="card card--back" aria-label="Card back">
    <div class="back-band"></div>
    <div class="name-block">
      <div class="person">Owen Hartley</div>
      <div class="role">Director</div>
    </div>
    <ul class="contact-list">
      <li class="address">#45 Alder Row, Fenwick City, 20418</li>
      <li class="phone">555.014.2270</li>
      <li class="phone">555.014.2270</li>
      <li class="email">name@kestrelventures.com</li>
      <li class="web">www.kestrelventures.com</li>
    </ul>
    <div class="back-mark">Kestrel<span>Ventures</span></div>
  </section>
</body>
</html>
```